VELMORAIR Business Card

We need a new elegant business card.
We are a company of business jet.
In attachment the old business card (2 sides) and the new logo.

Our adress is :
Aéroport de Brévillac la Combe - Bât.206
64390 TOUSSUS LE NOBLE - FRANCE

Target Market(s)

Lux

Industry/Entity Type

Business

Contact Information for Business Card

You can see the example in attachment

Font styles to use
Serif
Sans Serif

Requirements
Must have
• The color of the logo (white, black, blue)

```html
<!DOCTYPE html>
<html lang="en">
<head>
<meta charset="utf-8">
<title>VELMORAIR Business Card</title>
<link rel="stylesheet" href="https://fonts.googleapis.com/css2?family=Montserrat:wght@500;700;800&family=Open+Sans:ital,wght@1,700&family=Tinos&display=swap">
<style>
  :root {
    --stage: #3a3f45;
    --ink: #0b0b0b;
    --paper: #ffffff;
    --sky: #29a6e0;
    --sky-deep: #1f97d6;
    --mist: #b9bcc0;
  }
  html, body {
    margin: 0;
    width: 1200px;
    height: 900px;
    overflow: hidden;
    background: var(--stage);
  }
  .canvas { position: relative; width: 1200px; height: 900px; }
  .card {
    position: absolute;
    display: block;
    box-shadow: 0 12px 22px rgba(0,0,0,.45);
  }
  .card--front-white { left: 487px; top: 20px; }
  .card--back-black { left: 106px; top: 305px; }
  .card--front-blue { left: 348px; top: 592px; }
  .brand { font-family: "Montserrat", Arial, sans-serif; font-weight: 800; font-size: 30px; letter-spacing: 1px; }
  .holder-name { font-family: "Montserrat", Arial, sans-serif; font-weight: 500; font-size: 18px; }
  .holder-role { font-family: "Montserrat", Arial, sans-serif; font-weight: 500; font-size: 12px; }
  .contact { font-family: "Tinos", "Times New Roman", serif; font-size: 18px; letter-spacing: 1.4px; }
  .address { font-family: "Montserrat", Arial, sans-serif; font-weight: 500; font-size: 13.5px; }
  .tagline { font-family: "Open Sans", Arial, sans-serif; font-style: italic; font-weight: 700; font-size: 17px; }
</style>
</head>
<body>
<main class="canvas">

  <!-- Front, white edition -->
  <svg class="card card--front-white" width="584" height="272" viewBox="0 0 584 272" aria-label="Business card front, white">
    <rect width="584" height="272" fill="var(--paper)"/>
    <path d="M10 74 C120 22 250 28 360 62 S520 104 584 52" fill="none" stroke="var(--ink)" stroke-width="3"/>
    <path d="M400 76 C470 98 540 90 584 52" fill="none" stroke="var(--mist)" stroke-width="1.5"/>
    <circle cx="22" cy="149" r="82" fill="var(--ink)" stroke="var(--sky)" stroke-width="9"/>
    <rect x="0" y="0" width="10" height="272" fill="var(--sky)"/>
    <text class="brand" x="543" y="48" text-anchor="end" fill="var(--ink)">VELMORAIR</text>
    <text class="holder-name" x="109" y="77" fill="var(--ink)">LUCIEN MARAIS</text>
    <text class="holder-role" x="129" y="92" fill="var(--ink)">President/Captin</text>
    <g class="contact" fill="var(--ink)">
      <text x="168" y="132">Tel.</text><text x="236" y="132">:+33 (0) 1 42 18 07 35</text>
      <text x="168" y="155">Fax</text><text x="236" y="155">:+33 (0) 1 42 18 54 90</text>
      <text x="168" y="178">Mob.</text><text x="236" y="178">:+33 (0) 6 58 34 12 76</text>
      <text x="168" y="200">Email</text><text x="236" y="200">:lm@velmorair.com</text>
    </g>
    <rect x="10" y="242" width="574" height="30" fill="var(--ink)"/>
    <text class="address" x="23" y="261" fill="var(--paper)">Aéroport de Brévillac la Combe - Bât.206 - 64390 BRÉVILLAC - FRANCE</text>
  </svg>

  <!-- Back, black edition -->
  <svg class="card card--back-black" width="582" height="272" viewBox="0 0 582 272" aria-label="Business card back, black">
    <rect width="582" height="272" fill="var(--ink)"/>
    <path d="M21 58 C130 18 250 24 360 58 S520 96 582 46" fill="none" stroke="var(--paper)" stroke-width="2.5"/>
    <path d="M400 72 C470 90 540 82 582 46" fill="none" stroke="var(--mist)" stroke-width="1.2"/>
    <circle cx="33" cy="135" r="70" fill="var(--paper)" stroke="var(--sky)" stroke-width="7"/>
    <rect x="0" y="0" width="11" height="272" fill="var(--sky)"/>
    <rect x="11" y="0" width="10" height="272" fill="var(--paper)"/>
    <text class="brand" x="544" y="45" text-anchor="end" fill="var(--paper)">VELMORAIR</text>
    <text class="tagline" x="329" y="137" text-anchor="middle" fill="var(--paper)">Book Your Privet Jet Online</text>
    <text class="tagline" x="321" y="174" text-anchor="middle" fill="var(--paper)">www.velmorair.com</text>
    <text class="tagline" x="91" y="255" fill="var(--paper)" xml:space="preserve">Paris  -  London  -  Lyon  -  Geneva  -  Cannes</text>
  </svg>

  <!-- Front, blue edition -->
  <svg class="card card--front-blue" width="585" height="281" viewBox="0 0 585 281" aria-label="Business card front, blue">
    <defs>
      <linearGradient id="sky-wash" x1="0" y1="0" x2="0" y2="1">
        <stop offset="0" stop-color="var(--sky)"/>
        <stop offset="1" stop-color="var(--sky-deep)"/>
      </linearGradient>
    </defs>
    <rect width="585" height="281" fill="var(--paper)"/>
    <rect x="20" y="0" width="565" height="244" fill="url(#sky-wash)"/>
    <path d="M20 68 C130 24 250 30 360 64 S520 104 585 54" fill="none" stroke="var(--paper)" stroke-width="2.5"/>
    <path d="M400 78 C470 98 540 90 585 54" fill="none" stroke="var(--paper)" stroke-width="1.2" opacity=".7"/>
    <circle cx="29" cy="140" r="75" fill="var(--paper)" stroke="var(--ink)" stroke-width="7"/>
    <rect x="0" y="0" width="10" height="281" fill="var(--ink)"/>
    <text class="brand" x="545" y="48" text-anchor="end" fill="var(--paper)">VELMORAIR</text>
    <text class="holder-name" x="108" y="79" fill="var(--paper)">LUCIEN MARAIS</text>
    <text class="holder-role" x="128" y="96" fill="var(--paper)">President/Captin</text>
    <g class="contact" fill="var(--paper)">
      <text x="168" y="137">Tel.</text><text x="236" y="137">:+33 (0) 1 42 18 07 35</text>
      <text x="168" y="161">Fax</text><text x="236" y="161">:+33 (0) 1 42 18 54 90</text>
      <text x="168" y="184">Mob.</text><text x="236" y="184">:+33 (0) 6 58 34 12 76</text>
      <text x="168" y="207">Email</text><text x="236" y="207">:lm@velmorair.com</text>
    </g>
    <text class="address" x="22" y="270" fill="var(--ink)">Aéroport de Brévillac la Combe - Bât.206 - 64390 BRÉVILLAC - FRANCE</text>
  </svg>

</main>
</body>
</html>
```